Business Card Design Project

Hi Designers, this project is currently on hold until the Logo is completed:
Please submit to the Logo project here:
http://work.pitchvault.example/brief.aspx?id=413907

Once logo is completed, it will be attached to this project for you to create business cards with show logo, company name and address

Maren T R Quillby

Osric's Tiny Grey Heron Co.
Fernbrook
Nether Coombsby
North Devon EX91 4TZ

Tel: 01809 417356
Mobile: 07900 263818
email: maren@tiny-grey-heron.example.co.uk

Project Deadline Extended
Reason: Sorry everyone, we have had a sick ewe and I am now behind with this one and need to extend the deadline. Best wishes Maren

The designer who wins the logo brief will be asked to design the business card. Many thanks Maren

Project Deadline Extended
Reason: Sorry everyone, just a chaotic time of year with animals. Need to extend the deadline again..... as I just haven't had enough time to take a good look.... Thank you for your understanding. Maren

Project Deadline Extended
Reason: Sorry everyone It is our busiest time of year with animals and just no time to spend going through such great designs. I will have to extend the deadline again and hopefully have some news very soon. Wishing you all a very happy Christmas and a happy and healthy new year. Maren & Osric

High end market
Boutique restaurants for meat (it's not commercial lamb it's a slow matured quality meat more like venison/beef) expensive - specialized market

High End shoot clothing / wool / sheepskin rugs
Quality products

Business

• based on the logo - (which Pitch Vault has just been asked to do)
possibly based on a simplified picture of a Hebridean Ram (shows it's a Hebridean by it's horns as opposed to other black sheep!!)

```html
<!DOCTYPE html>
<html lang="en">
<head>
<meta charset="utf-8">
<title>Maren T R Quillby — Business Card</title>
<link href="https://fonts.googleapis.com/css2?family=Audiowide&family=Iceberg&display=swap" rel="stylesheet">
<style>
  :root {
    --card-bg: #000000;
    --ink: #ffffff;
    --frame-light: #d9d9d9;
    --frame-dark: #6e6e6e;
    --page-bg: #1a1a1a;
  }
  html, body {
    margin: 0;
    padding: 0;
    overflow: hidden;
    background: var(--page-bg);
  }
  .card {
    position: relative;
    width: 1200px;
    height: 633px;
    background: var(--card-bg);
    overflow: hidden;
    color: var(--ink);
    font-family: "Audiowide", sans-serif;
  }
  .card-frame {
    position: absolute;
    inset: 0;
    width: 1200px;
    height: 633px;
  }
  .brand-mark {
    position: absolute;
    left: 90px;
    top: 55px;
    width: 300px;
    height: 112px;
  }
  .brand-name {
    position: absolute;
    left: 60px;
    top: 196px;
    margin: 0;
    font-family: "Iceberg", sans-serif;
    font-size: 23px;
    font-weight: 400;
    letter-spacing: 1px;
    text-transform: uppercase;
  }
  .person-name {
    position: absolute;
    left: 562px;
    top: 90px;
    margin: 0;
    font-size: 44px;
    font-weight: 400;
    letter-spacing: 5px;
    text-transform: uppercase;
  }
  .address {
    position: absolute;
    left: 63px;
    top: 388px;
    margin: 0;
    font-style: normal;
    text-transform: uppercase;
    letter-spacing: 2px;
  }
  .address-company {
    display: block;
    font-size: 17px;
    line-height: 30px;
    margin-bottom: 4px;
  }
  .address-line {
    display: block;
    font-size: 26px;
    line-height: 43px;
  }
  .contact-list {
    position: absolute;
    left: 620px;
    top: 396px;
    margin: 0;
    padding: 0;
    list-style: none;
    text-transform: uppercase;
  }
  .contact-item {
    display: flex;
    align-items: center;
    height: 58px;
  }
  .contact-icon {
    width: 56px;
    height: 44px;
    flex: none;
    margin-right: 14px;
  }
  .contact-text {
    font-size: 24px;
    letter-spacing: 3px;
  }
  .contact-text--email {
    font-size: 16px;
    letter-spacing: 0.5px;
  }
</style>
</head>
<body>
  <main class="card">
    <svg class="card-frame" viewBox="0 0 1200 633" role="img" aria-label="Ornamental silver chain border framing the card">
      <defs>
        <linearGradient id="frameTone" x1="0" y1="0" x2="1" y2="1">
          <stop offset="0" stop-color="var(--frame-light)"/>
          <stop offset="0.5" stop-color="var(--frame-dark)"/>
          <stop offset="1" stop-color="var(--frame-light)"/>
        </linearGradient>
      </defs>
      <path fill="url(#frameTone)" fill-rule="evenodd"
        d="M10 6 H1190 V627 H10 Z M30 26 V607 H1170 V26 Z"/>
    </svg>

    <svg class="brand-mark" viewBox="0 0 300 112" aria-hidden="true">
      <ellipse cx="150" cy="56" rx="145" ry="52" fill="none" stroke="var(--ink)" stroke-width="7"/>
    </svg>
    <h2 class="brand-name">Osric's Tiny Grey Heron Co.</h2>

    <h1 class="person-name">Maren T R Quillby</h1>

    <address class="address">
      <span class="address-company">Osric's Tiny Grey Heron Co.</span>
      <span class="address-line">Fernbrook</span>
      <span class="address-line">Nether Coombsby</span>
      <span class="address-line">North Devon EX91 4TZ</span>
    </address>

    <ul class="contact-list">
      <li class="contact-item">
        <svg class="contact-icon" viewBox="0 0 56 44" aria-label="Telephone">
          <path d="M6 14 Q28 2 50 14 L46 20 L38 17 L38 13 Q28 10 18 13 L18 17 L10 20 Z" fill="none" stroke="var(--ink)" stroke-width="2.5" stroke-linejoin="round"/>
          <path d="M17 20 L39 20 L46 38 L10 38 Z" fill="none" stroke="var(--ink)" stroke-width="2.5" stroke-linejoin="round"/>
          <circle cx="28" cy="29" r="5" fill="none" stroke="var(--ink)" stroke-width="2"/>
        </svg>
        <span class="contact-text">01809 417356</span>
      </li>
      <li class="contact-item">
        <svg class="contact-icon" viewBox="0 0 56 44" aria-label="Mobile">
          <rect x="17" y="1" width="22" height="42" rx="4" fill="var(--ink)"/>
          <rect x="20" y="6" width="16" height="29" fill="var(--card-bg)"/>
          <circle cx="28" cy="39" r="1.8" fill="var(--card-bg)"/>
        </svg>
        <span class="contact-text">07900 263818</span>
      </li>
      <li class="contact-item">
        <svg class="contact-icon" viewBox="0 0 56 44" aria-label="Email">
          <rect x="5" y="8" width="46" height="30" fill="none" stroke="var(--ink)" stroke-width="3"/>
          <path d="M5 8 L28 26 L51 8" fill="none" stroke="var(--ink)" stroke-width="3"/>
          <path d="M5 38 L22 22 M51 38 L34 22" fill="none" stroke="var(--ink)" stroke-width="2"/>
        </svg>
        <span class="contact-text contact-text--email">maren@tiny-grey-heron.example.co.uk</span>
      </li>
    </ul>
  </main>
</body>
</html>
```